Fishing charter business in Sitka Alaska needs new business card design

I have had the same design for 10 plus years, ready for something different. I have attached a copy of my current card and my website link is www.tidecrestangling.example
I am looking for something that will catch my clients eye, although I rely on word of mouth for most of my business a a nice business card will help people remember who I am. My business is located in Sitka Alaska, there are probably 20-30 other charter businesses in Sitka. I like the way my current card is laid out, with the two tone black and grey. I can leave it up to the designers to come up with something else.
Target Market(s)
men, women, couples. Anyone who likes fishing
Industry/Entity Type
Tourism
Contact Information for Business Card
Dorvane's Charter Service
Kelpline Bay Sportfishing
Colors
Designer to choose colors to be used in the design.
Requirements
Must have
- Lyle Dorvane
- PO Box 4716
- Sitka, AK 99835
- Compass Rose image
- 100 Ton USCG Licensed Captain
- ldorvane@wavenet.example
- 907-555-0148
- www.tidecrestangling.example
Nice to have
- ghost image of "boat helm"
Should not have
- be to complex

```html
<!DOCTYPE html>
<html lang="en">
<head>
<meta charset="utf-8">
<title>Dorvane's Charter Service – Business Card</title>
<link href="https://fonts.googleapis.com/css2?family=Lato:wght@400;700;900&display=swap" rel="stylesheet">
<style>
  :root {
    --backdrop: #d9d9db;
    --card-charcoal: #2a2a2a;
    --card-black: #140909;
    --card-white: #ffffff;
    --ink: #1b1b1b;
    --ink-soft: #333333;
    --ghost: #3a3a3a;
    --paper-text: #f2f2f2;
  }
  * { box-sizing: border-box; margin: 0; padding: 0; }
  html, body {
    width: 1200px; height: 900px; overflow: hidden;
    background: var(--backdrop);
    font-family: "Lato", sans-serif;
  }
  .canvas { position: relative; width: 1200px; height: 900px; }

  .card {
    position: absolute;
    width: 600px; height: 340px;
    border-radius: 26px;
    overflow: hidden;
    box-shadow: 0 6px 18px rgba(0,0,0,0.18);
  }

  /* Back of card */
  .card-back {
    left: 90px; top: 100px;
    background: var(--card-charcoal);
    display: flex; align-items: center; justify-content: center;
  }
  .helm-ghost {
    position: absolute;
    left: 50%; top: 50%;
    width: 250px; height: 250px;
    transform: translate(-50%, -50%);
    border-radius: 50%;
    background: radial-gradient(circle, var(--ghost) 0%, rgba(58,58,58,0.5) 55%, rgba(42,42,42,0) 72%);
  }
  .back-brand { position: relative; text-align: center; color: var(--paper-text); }
  .back-brand .company {
    font-weight: 900; font-size: 29px; letter-spacing: 0.5px; text-transform: uppercase;
  }
  .back-brand .tagline {
    font-weight: 400; font-size: 15px; letter-spacing: 3.2px; text-transform: uppercase; margin-top: 2px;
  }

  /* Front of card */
  .card-front {
    left: 510px; top: 460px;
    background: var(--card-white);
    display: flex;
  }
  .compass-panel {
    width: 245px; height: 100%;
    background: var(--card-black);
    display: flex; align-items: center; justify-content: center;
  }
  .compass-rose {
    width: 170px; height: 170px; border-radius: 50%;
    background: radial-gradient(circle, #8a8585 0%, #4a4343 45%, #1e1414 72%);
  }
  .info-panel {
    flex: 1; padding: 42px 26px 0 30px; color: var(--ink);
  }
  .info-panel .company {
    font-weight: 900; font-size: 20px; text-transform: uppercase; letter-spacing: 0.2px;
  }
  .info-panel .tagline {
    font-size: 10.5px; letter-spacing: 2.1px; text-transform: uppercase; color: var(--ink-soft);
  }
  .captain { margin-top: 46px; }
  .captain .name { font-weight: 900; font-size: 18px; text-transform: uppercase; }
  .captain .title { font-size: 15px; }
  .contacts { list-style: none; margin-top: 6px; }
  .contacts li { display: flex; align-items: center; gap: 7px; font-size: 15px; line-height: 21px; }
  .contacts svg { width: 13px; height: 13px; flex: none; fill: var(--ink); }
  .address { font-size: 15px; margin-top: 10px; }
</style>
</head>
<body>
<main class="canvas">

  <section class="card card-back" aria-label="Card back">
    <div class="helm-ghost" role="img" aria-label="Faint ghost image of a boat helm"></div>
    <div class="back-brand">
      <div class="company">Dorvane's Charter Service</div>
      <div class="tagline">Kelpline Bay Sportfishing</div>
    </div>
  </section>

  <section class="card card-front" aria-label="Card front">
    <div class="compass-panel">
      <div class="compass-rose" role="img" aria-label="Hand-drawn compass rose with N, E, S, W points"></div>
    </div>
    <div class="info-panel">
      <div class="company">Dorvane's Charter Service</div>
      <div class="tagline">Kelpline Bay Sportfishing</div>

      <div class="captain">
        <div class="name">Lyle Dorvane</div>
        <div class="title">100 Ton USCG Licensed Captain</div>
      </div>

      <ul class="contacts">
        <li>
          <svg viewBox="0 0 16 16" aria-hidden="true"><path d="M3 1h3l1.5 3.5-2 1.3a9 9 0 0 0 4.7 4.7l1.3-2L15 10v3a2 2 0 0 1-2 2A12 12 0 0 1 1 3a2 2 0 0 1 2-2z"/></svg>
          907-555-0148
        </li>
        <li>
          <svg viewBox="0 0 16 16" aria-hidden="true"><path d="M1 3h14v10H1z M1.8 3.6 8 8.6l6.2-5" stroke="#fff" stroke-width="1.2"/></svg>
          ldorvane@wavenet.example
        </li>
        <li>
          <svg viewBox="0 0 16 16" aria-hidden="true"><circle cx="8" cy="8" r="7"/><path d="M1 8h14M8 1c-3 3.5-3 10.5 0 14M8 1c3 3.5 3 10.5 0 14" stroke="#fff" stroke-width="1" fill="none"/></svg>
          www.tidecrestangling.example
        </li>
      </ul>

      <div class="address">PO Box 4716 Sitka, AK 99835</div>
    </div>
  </section>

</main>
</body>
</html>
```